Realtor branding business card

modern, simple and self branding. Broker office logo needs to be used but not emphasized. Looking to brand myself

Target Market(s)

buyers, sellers and investors

Industry/Entity Type

Realtor

Contact Information for Business Card

Sample of my current business card on file

Requirements
Must have
• my website - emilioverdaskt.com
• Realtor logo
• Fair housing logo
Nice to have
• Colors from office logo but not a must
Should not have
• Do not want headshot

```html
<!DOCTYPE html>
<html lang="en">
<head>
<meta charset="utf-8">
<title>Emilio Verdaskt, PA – Business Card</title>
<link rel="stylesheet" href="https://fonts.googleapis.com/css2?family=Oswald:wght@500;600&family=Roboto:ital,wght@1,400&family=Questrial&display=swap">
<style>
:root{
  --ink:#2b2a2f;
  --paper:#ffffff;
  --red:#d9261c;
  --red-dark:#9e1a13;
  --blue:#0057a8;
  --blue-dark:#0b3566;
  --navy:#2d2a6e;
  --navy-dark:#1b1946;
  --badge:#4a4a4d;
  --light:#ffffff;
}
*{box-sizing:border-box;margin:0;padding:0}
html,body{width:1050px;height:1200px;overflow:hidden;background:var(--paper)}
.canvas{position:relative;width:1050px;height:1200px;background:var(--paper)}
.card{position:absolute;overflow:hidden;box-shadow:-4px 6px 10px rgba(0,0,0,.35)}
.card--front{left:148px;top:101px;width:758px;height:434px;background:var(--paper)}
.card--back{left:171px;top:669px;width:763px;height:444px;background:var(--ink)}
.front-shape{position:absolute;inset:0}
.brokerage{position:absolute;left:16px;top:26px;font-family:"Oswald",sans-serif;font-weight:600;color:var(--navy);line-height:1}
.brokerage__name{font-size:44px;letter-spacing:.5px}
.brokerage__sub{font-size:22px;letter-spacing:1px;margin-top:2px}
.agent{position:absolute;left:386px;width:320px;text-align:center;font-family:"Oswald",sans-serif}
.agent__name{top:50px;font-size:32px;font-weight:600;color:var(--light);letter-spacing:.5px}
.agent__title{top:94px;font-size:28px;font-weight:600;color:var(--red);letter-spacing:14px;padding-left:14px}
.contact{position:absolute;display:flex;align-items:center;color:var(--light);font-family:"Roboto",sans-serif;font-style:italic;box-shadow:2px 4px 5px rgba(0,0,0,.5)}
.contact--cell{left:224px;top:206px;width:467px;height:49px;background:var(--red)}
.contact--office{left:179px;top:286px;width:512px;height:50px;background:var(--blue)}
.contact--address{left:149px;top:366px;width:542px;height:49px;background:var(--navy)}
.contact svg{flex:none}
.contact__text{font-size:21px;letter-spacing:.5px}
.contact--address .contact__text{font-size:15px;line-height:1.3;letter-spacing:.6px}
.badges{position:absolute;left:34px;top:375px;display:flex;gap:18px}
.badge{width:34px;height:36px;background:var(--badge)}
.badge--round{border-radius:4px;width:40px;height:32px;margin-top:2px}
.back-name{position:absolute;left:0;right:0;top:92px;display:flex;align-items:center;justify-content:center;gap:22px;font-family:"Oswald",sans-serif;font-weight:600;color:var(--light);font-size:74px;letter-spacing:2px;line-height:1}
.back-name__mark{width:40px;height:40px;background:var(--red)}
.web-band{position:absolute;left:-3px;right:-3px;top:291px;height:46px;background:var(--red);display:flex;align-items:center;justify-content:center}
.web-band__url{font-family:"Questrial",sans-serif;color:var(--light);font-size:40px;letter-spacing:10px;padding-left:10px}
</style>
</head>
<body>
<main class="canvas">
  <section class="card card--front">
    <svg class="front-shape" width="758" height="434" viewBox="0 0 758 434" aria-hidden="true">
      <polygon points="364,0 758,0 758,434 160,434" fill="var(--ink)"/>
      <polygon points="224,206 273,194 273,206" fill="var(--red-dark)"/>
      <polygon points="179,286 235,273 235,286" fill="var(--blue-dark)"/>
      <polygon points="149,366 201,354 201,366" fill="var(--navy-dark)"/>
    </svg>
    <div class="brokerage">
      <div class="brokerage__name">Crestline</div>
      <div class="brokerage__sub">Realty Group</div>
    </div>
    <h1 class="agent agent__name">EMILIO VERDASKT, PA</h1>
    <p class="agent agent__title">REALTOR</p>
    <div class="contact contact--cell">
      <svg width="40" height="40" viewBox="0 0 24 24" style="margin:0 36px 0 52px" fill="none" stroke="var(--light)" stroke-width="1.4" stroke-linejoin="round"><path d="M6 3l3 4-2 2c1 3 4 6 7 7l2-2 4 3-2 3c-7 0-14-7-14-14z"/><path d="M14 3a7 7 0 0 1 7 7M14 6a4 4 0 0 1 4 4" stroke-linecap="round"/></svg>
      <span class="contact__text">Cell: 407.555.0142</span>
    </div>
    <div class="contact contact--office">
      <svg width="26" height="40" viewBox="0 0 16 26" style="margin:0 42px 0 68px" fill="none" stroke="var(--light)" stroke-width="1.6"><rect x="1" y="1" width="14" height="24" rx="2"/><line x1="1" y1="5" x2="15" y2="5"/><line x1="1" y1="20" x2="15" y2="20"/><circle cx="8" cy="22.5" r=".6" fill="var(--light)"/></svg>
      <span class="contact__text">Office: 407.555.0100</span>
    </div>
    <div class="contact contact--address">
      <svg width="44" height="40" viewBox="0 0 26 24" style="margin:0 32px 0 56px" fill="none" stroke="var(--light)" stroke-width="1.6" stroke-linejoin="round"><path d="M1 12L13 1l12 11"/><path d="M5 9v14h6v-7h4v7h6V9"/></svg>
      <span class="contact__text">140 Harbor Pointe Dr.<br>Maitland Springs, FL 32700</span>
    </div>
    <div class="badges">
      <span class="badge" role="img" aria-label="Realtor membership badge"></span>
      <span class="badge badge--round" role="img" aria-label="Equal housing opportunity badge"></span>
    </div>
  </section>

  <section class="card card--back">
    <div class="back-name"><span class="back-name__mark"></span><span>Crestline</span></div>
    <div class="web-band"><span class="web-band__url">emilioverdaskt.com</span></div>
  </section>
</main>
</body>
</html>
```